Harbor Crew Biz Cards

looking for a new catchy business card where my cell number is very prominent:
My pic and logo are attached. My whole picture isn't necessary if it makes more sense to crop it.

Info needed:

(Big) Marcus Pellton
(Medium) Real Estate Professional
(Medium) Buyer/Seller Specialist
(Big) Call/Text 410-739-2184
(small) Marcuspell@mailbrook.com
(small) www.harborcrewhomes.com

(very small)
The Harbor Crew
at Keystone Real Estate
2847 W Larkmoor Rd, Crestmoor, MD 21190
833-555-0192

```html
<!DOCTYPE html>
<html lang="en">
<head>
<meta charset="utf-8">
<title>Harbor Crew Business Cards</title>
<link rel="stylesheet" href="https://fonts.googleapis.com/css2?family=Lato:wght@700&family=Tenor+Sans&display=swap">
<style>
  :root {
    --navy: #0d2a55;
    --navy-deep: #020f2e;
    --navy-mid: #0a3063;
    --ink: #1b2f57;
    --grey-text: #4a4f5a;
    --silver: #9aa3b0;
    --card-white: #fbfbfb;
    --card-shade: #ececec;
    --backdrop: #e7e3de;
  }
  * { box-sizing: border-box; margin: 0; padding: 0; }
  html, body {
    width: 1200px; height: 900px; overflow: hidden;
    background: var(--backdrop);
  }
  .canvas { position: relative; width: 1200px; height: 900px; }
  .card {
    position: absolute; left: 250px; width: 700px; height: 400px;
    border-radius: 34px; overflow: hidden;
    box-shadow: 0 10px 28px rgba(0,0,0,0.22);
  }
  /* Back */
  .card-back {
    top: 35px;
    background: radial-gradient(ellipse at 30% 75%, var(--navy-mid) 0%, var(--navy) 40%, var(--navy-deep) 100%);
    display: flex; flex-direction: column; align-items: center; justify-content: center;
  }
  .brand {
    font-family: "Tenor Sans", sans-serif;
    text-transform: uppercase; text-align: center; letter-spacing: 0.06em;
  }
  .card-back .brand { color: var(--silver); }
  .brand-row { display: flex; align-items: center; gap: 14px; }
  .brand-dot { width: 16px; height: 16px; border-radius: 50%; background: currentColor; flex: none; }
  .card-back .brand-name { font-size: 46px; }
  .card-back .brand-sub { font-size: 15px; letter-spacing: 0.22em; margin-top: 10px; }

  /* Front */
  .card-front {
    top: 465px;
    background: linear-gradient(100deg, var(--card-shade) 0%, var(--card-white) 55%, #fff 100%);
  }
  .portrait {
    position: absolute; right: 0; top: 0; width: 200px; height: 400px;
    background: linear-gradient(180deg, #f4f4f6 0%, #2a3a5e 35%, #1d2740 75%, #f2f2f2 100%);
  }
  .details {
    position: absolute; right: 215px; top: 30px; width: 430px;
    text-align: right; font-family: "Tenor Sans", sans-serif; color: var(--grey-text);
  }
  .name { font-family: "Lato", sans-serif; font-weight: 700; font-size: 30px; color: var(--navy); }
  .role { font-size: 17px; margin-top: 4px; }
  .line { display: flex; justify-content: flex-end; align-items: center; gap: 8px; }
  .line svg { width: 18px; height: 18px; flex: none; }
  .spacer { width: 18px; flex: none; }
  .cell { font-size: 26px; color: var(--ink); margin-top: 16px; }
  .cell svg { width: 20px; height: 24px; }
  .web { font-size: 17px; margin-top: 3px; }
  .web.first { margin-top: 16px; }
  .office { font-size: 17px; color: var(--navy); margin-top: 16px; }
  .address { font-size: 16px; margin-top: 2px; }
  .card-front .brand {
    position: absolute; left: 40px; bottom: 30px; color: var(--navy); text-align: left;
  }
  .card-front .brand-name { font-size: 24px; }
  .card-front .brand-sub { font-size: 10px; letter-spacing: 0.2em; margin-top: 6px; }
  .card-front .brand-dot { width: 11px; height: 11px; }
  .icon { fill: none; stroke: var(--navy); stroke-width: 1.8; stroke-linecap: round; stroke-linejoin: round; }
  .icon-solid { fill: var(--navy); }
</style>
</head>
<body>
<main class="canvas">
  <section class="card card-back" aria-label="Card back">
    <div class="brand">
      <div class="brand-row"><span class="brand-dot"></span><span class="brand-name">The Harbor Crew</span></div>
      <div class="brand-sub">at Keystone Real Estate</div>
    </div>
  </section>

  <section class="card card-front" aria-label="Card front">
    <div class="details">
      <div class="name">Marcus Pellton</div>
      <div class="role">Real Estate Professional | Buyer/Seller Specialist</div>
      <div class="line cell">410-739-2184
        <svg viewBox="0 0 20 24"><rect class="icon" x="4" y="2" width="12" height="20" rx="2"/><line class="icon" x1="9" y1="18.5" x2="11" y2="18.5"/></svg>
      </div>
      <div class="line web first">Marcuspell@mailbrook.com
        <svg viewBox="0 0 18 18"><rect class="icon-solid" x="1" y="4" width="16" height="11" rx="1.5"/><polyline points="2,5 9,10 16,5" fill="none" stroke="#fff" stroke-width="1.4"/></svg>
      </div>
      <div class="line web">www.harborcrewhomes.com
        <svg viewBox="0 0 18 18"><circle class="icon" cx="9" cy="9" r="7"/><ellipse class="icon" cx="9" cy="9" rx="3" ry="7"/><line class="icon" x1="2" y1="9" x2="16" y2="9"/></svg>
      </div>
      <div class="line office">833-555-0192
        <svg viewBox="0 0 18 18"><path class="icon-solid" d="M2 7c0-2 3-4 7-4s7 2 7 4l-3 1-1-2H6L5 8z"/><rect class="icon-solid" x="4" y="9" width="10" height="6" rx="1"/></svg>
      </div>
      <div class="line address">2847 W Larkmoor Rd
        <svg viewBox="0 0 18 18"><path class="icon-solid" d="M9 1a5.5 5.5 0 0 1 5.5 5.5C14.5 11 9 17 9 17S3.5 11 3.5 6.5A5.5 5.5 0 0 1 9 1z"/><circle cx="9" cy="6.5" r="2" fill="#fff"/></svg>
      </div>
      <div class="line address">Crestmoor, MD 21190<span class="spacer"></span></div>
    </div>

    <div class="portrait" role="img" aria-label="Full-length photo of the agent in a navy suit on a white background"></div>

    <div class="brand">
      <div class="brand-row"><span class="brand-dot"></span><span class="brand-name">The Harbor Crew</span></div>
      <div class="brand-sub">at Keystone Real Estate</div>
    </div>
  </section>
</main>
</body>
</html>
```